New Web Site - Professional Cleaning Company

I want to create a new attractive website that acts as an advertisement to visitors to entice them to reach out for more information.
We are a commercial/business janitorial service - with a new logo, would like the font to be complimentary to the font of logo, as well as the color scheme.
Target Market(s)
Commercial buildings, schools & medical buildings
Industry/Entity Type
Janitorial
Coding
Coded - Design and coding required
Number of Pages Required
4 page
Requirements
Must have
- Professionalism, sharp imagery

```html
<!DOCTYPE html>
<html lang="en">
<head>
<meta charset="utf-8">
<title>Brightwell Facility</title>
<link href="https://fonts.googleapis.com/css2?family=Nunito:wght@400;600;700;800&display=swap" rel="stylesheet">
<style>
:root{
  --ink:#1c2233;
  --text:#3a3f4e;
  --muted:#8a8f99;
  --rust:#b8410f;
  --blue:#2b63f5;
  --link:#3d6cf0;
  --wash:#eaf5f8;
  --card:#f1f8fa;
  --band:#4e5163;
  --line:#dfe3ea;
  --star:#f2c53d;
  --quote:#c98670;
  --white:#ffffff;
}
*{margin:0;padding:0;box-sizing:border-box}
html,body{width:1200px;height:3125px;overflow:hidden;background:var(--white)}
body{position:relative;font-family:'Nunito',sans-serif;color:var(--text)}
.abs{position:absolute}
.waves{position:absolute;left:0;top:0;width:1200px;height:3125px}

.why-title{left:76px;top:28px;font-size:31px;font-weight:800;color:var(--ink)}
.why-title span{color:var(--rust)}
.why-copy{left:95px;top:103px;width:500px;font-size:13px;font-weight:700;line-height:23px;color:#4a4f5c}
.why-copy p+p{margin-top:7px}
.checklist{left:109px;top:234px;list-style:none}
.checklist li{height:41px;font-size:14px;font-weight:700;color:#4a4f5c;display:flex;align-items:center;gap:9px}
.checklist svg{flex:none}
.hero-backdrop{left:621px;top:254px;width:506px;height:203px;border-radius:18px;background:var(--wash)}
.hero-photo{left:742px;top:0;width:392px;height:457px;border-radius:0 0 14px 14px;background:linear-gradient(180deg,#d9e9ee 0%,#9fd3d6 55%,#7cc7d8 100%)}

.section-title{left:0;width:1200px;text-align:center;font-size:31px;font-weight:800;letter-spacing:2.5px;color:var(--ink)}
.section-title span{color:var(--rust)}

.t-card{background:var(--card);border-radius:10px;box-shadow:0 2px 10px rgba(0,0,0,.12);text-align:center;padding:0 46px}
.t-card.featured{background:var(--white);padding:0 46px}
.t-quote{font-size:56px;font-weight:800;color:var(--quote);height:40px;line-height:66px;margin-top:24px}
.t-text{font-size:11px;letter-spacing:1px;line-height:17px;color:var(--muted);margin-top:30px}
.featured .t-text{font-size:12px;line-height:18px;color:#22262f;margin-top:34px}
.t-name{font-size:11px;letter-spacing:1px;font-weight:700;color:#22262f;margin-top:30px;white-space:nowrap}
.t-role{font-size:11px;font-weight:600;color:#22262f;margin:6px -40px 0;white-space:nowrap}
.t-role a{color:var(--link);text-decoration:none}
.t-avatar{width:84px;height:84px;border-radius:50%;border:2px solid #2a6b75;margin:8px auto 0;background:linear-gradient(160deg,#d5dce0,#7a8389)}
.featured .t-avatar{width:90px;height:90px}
.t-stars{display:flex;justify-content:center;gap:3px;margin-top:4px}
.nav-arrow{top:872px}

.faq-item{left:150px;width:899px;height:73px;border:1.5px solid var(--line);border-radius:8px;background:var(--white);padding:0 29px;display:flex;align-items:center;justify-content:space-between;font-size:18px;font-weight:600;letter-spacing:.6px;color:#23283a}
.faq-item.open{height:177px;border-color:#8aa8f6;display:block;padding-top:22px}
.faq-item.open .faq-q{color:var(--link);display:flex;justify-content:space-between;align-items:center}
.faq-a{margin-top:20px;font-size:18px;font-weight:500;line-height:27px;color:#2c3140}

.still-title{left:0;top:1914px;width:1200px;text-align:center;font-size:31px;font-weight:800;letter-spacing:1.5px;color:#11151f}
.still-copy{left:0;top:1970px;width:1200px;text-align:center;font-size:13px;letter-spacing:.8px;line-height:22px;color:#5a5f6b}
.still-copy a{color:var(--rust);text-decoration:underline}

.cta-band{left:75px;top:2100px;width:1049px;height:187px;border-radius:22px;background:var(--band);box-shadow:0 4px 12px rgba(0,0,0,.2);color:var(--white)}
.cta-lead{left:56px;top:36px;font-size:23px;font-weight:700;letter-spacing:1.2px}
.cta-copy{left:56px;top:80px;width:640px;font-size:21px;font-weight:700;letter-spacing:1.2px;line-height:36px}
.cta-button{left:806px;top:100px;width:187px;height:51px;border-radius:14px;background:var(--white);color:var(--link);font-size:18px;font-weight:800;letter-spacing:1px;display:flex;align-items:center;justify-content:center}

.partners{left:75px;top:2480px;width:1050px;display:flex;justify-content:space-between;align-items:center}
.partner{display:flex;align-items:center;gap:12px;font-size:34px;font-weight:800;color:#2a2d36}
.partner i{display:block;width:44px;height:44px;border-radius:50%;background:#2a2d36}

.contact-card{left:750px;top:2608px;width:374px;height:449px;background:var(--white);box-shadow:0 2px 12px rgba(0,0,0,.14)}
.contact-card h3{position:absolute;left:22px;top:22px;width:300px;font-size:17px;font-weight:800;letter-spacing:2px;line-height:27px;color:#23283a}
.field{position:absolute;left:18px;width:337px;height:55px;background:var(--wash);border-radius:3px;font-size:13px;font-weight:600;letter-spacing:.8px;color:#4a4f5c;padding-left:15px;display:flex;align-items:center}
.send-btn{position:absolute;left:102px;top:383px;width:171px;height:43px;border-radius:22px;background:var(--blue);color:var(--white);font-size:12px;font-weight:700;letter-spacing:1px;display:flex;align-items:center;justify-content:center}

.brand{left:75px;top:2810px;display:flex;align-items:center;gap:8px;font-size:17px;font-weight:800;color:#1f4f8f}
.brand i{display:block;width:22px;height:22px;border-radius:50%;background:#1f4f8f}
.tagline{left:75px;top:2903px;width:220px;font-size:12px;font-weight:700;letter-spacing:1px;line-height:18px;color:#1c2233}
.follow{left:108px;top:2969px;font-size:12px;font-weight:700;letter-spacing:1px;color:#1c2233}
.social{top:3000px;width:32px;height:32px;border-radius:50%;background:var(--white);border:1.5px solid #c9d4ea}
.footer-contact{left:388px;top:2915px;font-size:12px;letter-spacing:1px;color:#4a4f5c}
.footer-contact h4{font-size:12px;font-weight:700;color:#1c2233;margin-bottom:7px}
.footer-contact p{display:flex;align-items:center;gap:5px;height:21px}
.copyright{left:0;top:3096px;width:1200px;text-align:center;font-size:11px;letter-spacing:1px;color:#4a4f5c}
</style>
</head>
<body>

<svg class="waves" viewBox="0 0 1200 3125" aria-hidden="true">
  <path d="M0 740 C180 800 330 760 520 700 C760 620 1000 560 1200 510 L1200 1420 C1100 1330 980 1240 760 1170 C560 1110 380 1080 0 1040 Z" fill="#eaf5f8"/>
  <path d="M0 2905 C300 2870 560 2700 800 2610 C950 2560 1080 2550 1200 2530 L1200 3125 L0 3125 Z" fill="#eaf5f8"/>
</svg>

<!-- Why section -->
<h1 class="abs why-title"><span>Why</span> Brightwell Facility</h1>
<div class="abs why-copy">
  <p>We know letting a crew into your building is a big deal. All Lakeview Facility Services cleaners are carefully vetted by us so we choose the right team to care for your site.</p>
  <p>We guarantee your Lakeview Facility Services cleaning crew will always be:</p>
</div>
<ul class="abs checklist">
  <li><svg width="15" height="15" viewBox="0 0 15 15"><rect x="1" y="1" width="13" height="13" rx="3" fill="none" stroke="#d98a6e" stroke-width="1.4"/><path d="M4 7.5l2.5 2.5L11 5" fill="none" stroke="#d98a6e" stroke-width="1.5"/></svg>Lorem ipsum dolor sit amet, consectetur</li>
  <li><svg width="15" height="15" viewBox="0 0 15 15"><rect x="1" y="1" width="13" height="13" rx="3" fill="none" stroke="#d98a6e" stroke-width="1.4"/><path d="M4 7.5l2.5 2.5L11 5" fill="none" stroke="#d98a6e" stroke-width="1.5"/></svg>Lorem ipsum dolor sit amet, consectetur</li>
  <li><svg width="15" height="15" viewBox="0 0 15 15"><rect x="1" y="1" width="13" height="13" rx="3" fill="none" stroke="#d98a6e" stroke-width="1.4"/><path d="M4 7.5l2.5 2.5L11 5" fill="none" stroke="#d98a6e" stroke-width="1.5"/></svg>Lorem ipsum dolor sit amet, consectetur</li>
  <li><svg width="15" height="15" viewBox="0 0 15 15"><rect x="1" y="1" width="13" height="13" rx="3" fill="none" stroke="#d98a6e" stroke-width="1.4"/><path d="M4 7.5l2.5 2.5L11 5" fill="none" stroke="#d98a6e" stroke-width="1.5"/></svg>Lorem ipsum dolor sit amet, consectetur</li>
  <li><svg width="15" height="15" viewBox="0 0 15 15"><rect x="1" y="1" width="13" height="13" rx="3" fill="none" stroke="#d98a6e" stroke-width="1.4"/><path d="M4 7.5l2.5 2.5L11 5" fill="none" stroke="#d98a6e" stroke-width="1.5"/></svg>Lorem ipsum dolor sit amet, consectetur</li>
  <li><svg width="15" height="15" viewBox="0 0 15 15"><rect x="1" y="1" width="13" height="13" rx="3" fill="none" stroke="#d98a6e" stroke-width="1.4"/><path d="M4 7.5l2.5 2.5L11 5" fill="none" stroke="#d98a6e" stroke-width="1.5"/></svg>Lorem ipsum dolor sit amet, consectetur</li>
</ul>
<div class="abs hero-backdrop"></div>
<div class="abs hero-photo" role="img" aria-label="Photo of a smiling janitorial team member in an apron holding a spray bottle and a mop"></div>

<!-- Testimonials -->
<h2 class="abs section-title" style="top:560px">Testimonials</h2>

<svg class="abs nav-arrow" style="left:98px" width="28" height="54" viewBox="0 0 28 54" aria-hidden="true"><path d="M22 4L6 27l16 23" fill="none" stroke="#8a8f99" stroke-width="6" stroke-linecap="round" stroke-linejoin="round"/></svg>
<svg class="abs nav-arrow" style="left:1074px" width="28" height="54" viewBox="0 0 28 54" aria-hidden="true"><path d="M6 4l16 23L6 50" fill="none" stroke="#2b63f5" stroke-width="6" stroke-linecap="round" stroke-linejoin="round"/></svg>

<div class="abs t-card" style="left:158px;top:679px;width:270px;height:442px">
  <div class="t-quote">“</div>
  <p class="t-text">Lorem ipsum dolor sit amet, consectetur adipiscing elit, sed do eiusmod tempor incididunt ut labore et dolore magna aliqua. Quis ipsum suspendisse ultrices gravida. Risus commodo viverra maecenas accumsan lacus vel facilisis.</p>
  <p class="t-name">Dana M. Ortiz</p>
  <p class="t-role">CEO and Co-Founder of <a>socialhub.example</a></p>
  <div class="t-avatar" role="img" aria-label="Client portrait"></div>
  <div class="t-stars">
    <svg width="20" height="20" viewBox="0 0 20 20"><path d="M10 1l2.7 5.9 6.3.6-4.8 4.3 1.4 6.3L10 14.8 4.4 18.1l1.4-6.3L1 7.5l6.3-.6z" fill="#f2c53d"/></svg><svg width="20" height="20" viewBox="0 0 20 20"><path d="M10 1l2.7 5.9 6.3.6-4.8 4.3 1.4 6.3L10 14.8 4.4 18.1l1.4-6.3L1 7.5l6.3-.6z" fill="#f2c53d"/></svg><svg width="20" height="20" viewBox="0 0 20 20"><path d="M10 1l2.7 5.9 6.3.6-4.8 4.3 1.4 6.3L10 14.8 4.4 18.1l1.4-6.3L1 7.5l6.3-.6z" fill="#f2c53d"/></svg><svg width="20" height="20" viewBox="0 0 20 20"><path d="M10 1l2.7 5.9 6.3.6-4.8 4.3 1.4 6.3L10 14.8 4.4 18.1l1.4-6.3L1 7.5l6.3-.6z" fill="#f2c53d"/></svg><svg width="20" height="20" viewBox="0 0 20 20"><path d="M10 1l2.7 5.9 6.3.6-4.8 4.3 1.4 6.3L10 14.8 4.4 18.1l1.4-6.3L1 7.5l6.3-.6z" fill="#f2c53d"/></svg>
  </div>
</div>

<div class="abs t-card featured" style="left:458px;top:667px;width:284px;height:465px">
  <div class="t-quote">“</div>
  <p class="t-text">Lorem ipsum dolor sit amet, consectetur adipiscing elit, sed do eiusmod tempor incididunt ut labore et dolore magna aliqua. Quis ipsum suspendisse ultrices gravida. Risus commodo viverra maecenas accumsan lacus vel facilisis.</p>
  <p class="t-name">Dana M. Ortiz</p>
  <p class="t-role">CEO and Co-Founder of <a>socialhub.example</a></p>
  <div class="t-avatar" role="img" aria-label="Client portrait"></div>
  <div class="t-stars">
    <svg width="22" height="22" viewBox="0 0 20 20"><path d="M10 1l2.7 5.9 6.3.6-4.8 4.3 1.4 6.3L10 14.8 4.4 18.1l1.4-6.3L1 7.5l6.3-.6z" fill="#f2c53d"/></svg><svg width="22" height="22" viewBox="0 0 20 20"><path d="M10 1l2.7 5.9 6.3.6-4.8 4.3 1.4 6.3L10 14.8 4.4 18.1l1.4-6.3L1 7.5l6.3-.6z" fill="#f2c53d"/></svg><svg width="22" height="22" viewBox="0 0 20 20"><path d="M10 1l2.7 5.9 6.3.6-4.8 4.3 1.4 6.3L10 14.8 4.4 18.1l1.4-6.3L1 7.5l6.3-.6z" fill="#f2c53d"/></svg><svg width="22" height="22" viewBox="0 0 20 20"><path d="M10 1l2.7 5.9 6.3.6-4.8 4.3 1.4 6.3L10 14.8 4.4 18.1l1.4-6.3L1 7.5l6.3-.6z" fill="#f2c53d"/></svg><svg width="22" height="22" viewBox="0 0 20 20"><path d="M10 1l2.7 5.9 6.3.6-4.8 4.3 1.4 6.3L10 14.8 4.4 18.1l1.4-6.3L1 7.5l6.3-.6z" fill="#f2c53d"/></svg>
  </div>
</div>

<div class="abs t-card" style="left:771px;top:679px;width:271px;height:442px">
  <div class="t-quote">“</div>
  <p class="t-text">Lorem ipsum dolor sit amet, consectetur adipiscing elit, sed do eiusmod tempor incididunt ut labore et dolore magna aliqua. Quis ipsum suspendisse ultrices gravida. Risus commodo viverra maecenas accumsan lacus vel facilisis.</p>
  <p class="t-name">Dana M. Ortiz</p>
  <p class="t-role">CEO and Co-Founder of <a>socialhub.example</a></p>
  <div class="t-avatar" role="img" aria-label="Client portrait"></div>
  <div class="t-stars">
    <svg width="20" height="20" viewBox="0 0 20 20"><path d="M10 1l2.7 5.9 6.3.6-4.8 4.3 1.4 6.3L10 14.8 4.4 18.1l1.4-6.3L1 7.5l6.3-.6z" fill="#f2c53d"/></svg><svg width="20" height="20" viewBox="0 0 20 20"><path d="M10 1l2.7 5.9 6.3.6-4.8 4.3 1.4 6.3L10 14.8 4.4 18.1l1.4-6.3L1 7.5l6.3-.6z" fill="#f2c53d"/></svg><svg width="20" height="20" viewBox="0 0 20 20"><path d="M10 1l2.7 5.9 6.3.6-4.8 4.3 1.4 6.3L10 14.8 4.4 18.1l1.4-6.3L1 7.5l6.3-.6z" fill="#f2c53d"/></svg><svg width="20" height="20" viewBox="0 0 20 20"><path d="M10 1l2.7 5.9 6.3.6-4.8 4.3 1.4 6.3L10 14.8 4.4 18.1l1.4-6.3L1 7.5l6.3-.6z" fill="#f2c53d"/></svg><svg width="20" height="20" viewBox="0 0 20 20"><path d="M10 1l2.7 5.9 6.3.6-4.8 4.3 1.4 6.3L10 14.8 4.4 18.1l1.4-6.3L1 7.5l6.3-.6z" fill="#f2c53d"/></svg>
  </div>
</div>

<!-- FAQ -->
<h2 class="abs section-title" style="top:1253px">Frequently asked <span>questions</span></h2>

<div class="abs faq-item" style="top:1348px">How much does janitorial service cost at Brightwell Facility?<svg width="14" height="8" viewBox="0 0 14 8"><path d="M0 0h14L7 8z" fill="#6d7280"/></svg></div>
<div class="abs faq-item" style="top:1438px">How does the cleaning crew access our building?<svg width="14" height="8" viewBox="0 0 14 8"><path d="M0 0h14L7 8z" fill="#6d7280"/></svg></div>
<div class="abs faq-item" style="top:1528px">Do we need to do anything before the janitorial crew arrives?<svg width="14" height="8" viewBox="0 0 14 8"><path d="M0 0h14L7 8z" fill="#6d7280"/></svg></div>
<div class="abs faq-item open" style="top:1618px">
  <div class="faq-q">Do we need to prepare for an end-of-lease office clean?<svg width="14" height="8" viewBox="0 0 14 8"><path d="M0 8h14L7 0z" fill="#3d6cf0"/></svg></div>
  <p class="faq-a">Yes, please;<br>we need electricity and water to clean, so please make sure your utilities<br>are still functioning.</p>
</div>
<div class="abs faq-item" style="top:1813px">Do you pay your employees well?<svg width="14" height="8" viewBox="0 0 14 8"><path d="M0 0h14L7 8z" fill="#6d7280"/></svg></div>

<h2 class="abs still-title">Still have a question?</h2>
<p class="abs still-copy">If you cannot find answer to your question in our FAQ, you can always<br><a>contact us</a>. We will answer to you shortly!</p>

<!-- Call to action -->
<div class="abs cta-band">
  <p class="abs cta-lead">How can we take care of your facility?</p>
  <p class="abs cta-copy">Tell us about your building, and get a price with no on-site consultation. Right now.</p>
  <div class="abs cta-button">Get a price</div>
</div>

<!-- Partners -->
<h2 class="abs section-title" style="top:2388px"><span>Our</span> trusted partners</h2>
<div class="abs partners">
  <div class="partner"><i></i>Northline</div>
  <div class="partner"><i></i>Crestway</div>
  <div class="partner"><i></i>Orbitek</div>
  <div class="partner"><i></i>Pinefield</div>
</div>

<!-- Footer -->
<div class="abs brand"><i></i>Brightwell</div>
<p class="abs tagline">Because your workplace deserves to be clean.</p>
<p class="abs follow">Follow Us:</p>
<div class="abs social" style="left:109px"></div>
<div class="abs social" style="left:157px"></div>

<div class="abs footer-contact">
  <h4>Contact Us</h4>
  <p><svg width="11" height="11" viewBox="0 0 12 12"><path d="M2.5 1l2 2.5-1 1.3c.7 1.5 1.8 2.6 3.2 3.2l1.3-1 2.5 2-.9 1.8C5 10.5 1.5 7 .8 2z" fill="#2b63f5"/></svg>555-010-0270</p>
  <p><svg width="11" height="11" viewBox="0 0 12 12"><rect x="0.5" y="2" width="11" height="8" rx="1" fill="#2b63f5"/><path d="M1 2.5l5 4 5-4" fill="none" stroke="#fff" stroke-width="1"/></svg>contact@brightwellfacility.example</p>
  <p><svg width="11" height="11" viewBox="0 0 12 12"><path d="M6 0.5a3.5 3.5 0 0 1 3.5 3.5C9.5 6.5 6 10 6 10S2.5 6.5 2.5 4A3.5 3.5 0 0 1 6 .5z" fill="#2b63f5"/><circle cx="6" cy="4" r="1.3" fill="#fff"/><rect x="1" y="10.3" width="10" height="1.2" fill="#2b63f5"/></svg>1200, 45 Maple Row, Fairview, FL. USA</p>
</div>

<div class="abs contact-card">
  <h3>Send us an email to contact us.</h3>
  <div class="field" style="top:86px">Enter your full name</div>
  <div class="field" style="top:156px">Enter your E-mail adress</div>
  <div class="field" style="top:228px">Enter your phone number</div>
  <div class="field" style="top:303px">How can we help you ?</div>
  <div class="send-btn">Contact Us</div>
</div>

<p class="abs copyright">Copyright © 2020-2021 Brightwell Facility . All rights reserved.</p>

</body>
</html>
```